New Business Card for Auto Repair and Performance Shop!

Need a redesign on a card that we have used for a while now. Something more update and modern, Serious but not too serious. Something confident, that shows the client that we are bespoke. Adding value.

Target Market(s)

Foreign Auto Repair and Performance

Industry/Entity Type

Automotive

Contact Information for Business Card

Utilize Logo, would like to change car silhouette to something Veltra,

Font styles to use
Sans Serif

Requirements
Must have
• business name, address, website, phone number.
MotoSerenix
4918 W. Birchwell Rd
Killeen, T.X. 76542
1-254-487-3106
www.moto-serenix-example.com

Specializing in Asian, European, and Domestic Auto Repair, Performance and Fabrication.

Clear space on back to for space to write appointment time and which client advisor helped the client.
Nice to have
• Up to the designers,

```html
<!DOCTYPE html>
<html lang="en">
<head>
<meta charset="utf-8">
<title>MotoSerenix – Business Card</title>
<link rel="stylesheet" href="https://fonts.googleapis.com/css2?family=Arimo:wght@400&display=swap">
<style>
  :root {
    --red-top: #e80000;
    --red-mid: #d60000;
    --red-bottom: #990000;
    --ink: #ffffff;
    --ink-soft: rgba(255, 255, 255, 0.82);
    --rule: rgba(255, 255, 255, 0.7);
  }
  html, body {
    margin: 0;
    padding: 0;
    width: 703px;
    height: 1200px;
    overflow: hidden;
    background: var(--red-bottom);
  }
  .card {
    position: relative;
    width: 703px;
    height: 1200px;
    overflow: hidden;
    background: linear-gradient(180deg,
      var(--red-top) 0%,
      var(--red-top) 38%,
      var(--red-mid) 52%,
      var(--red-bottom) 100%);
    font-family: "Arimo", Arial, sans-serif;
    color: var(--ink);
  }

  /* Brand block */
  .brand {
    position: absolute;
    left: 0;
    right: 0;
    top: 258px;
    margin: 0;
    text-align: center;
    font-size: 58px;
    font-weight: 400;
    letter-spacing: 2px;
    line-height: 1;
  }
  .specialty {
    position: absolute;
    left: 80px;
    right: 80px;
    top: 350px;
    margin: 0;
    text-align: center;
    font-size: 18px;
    letter-spacing: 1.5px;
    line-height: 28px;
    color: var(--ink-soft);
  }

  /* Appointment space */
  .appointment {
    position: absolute;
    left: 110px;
    right: 110px;
    top: 520px;
  }
  .appointment-title {
    margin: 0 0 34px;
    text-align: center;
    font-size: 20px;
    letter-spacing: 4px;
    text-transform: uppercase;
    font-weight: 400;
  }
  .field {
    display: flex;
    align-items: flex-end;
    height: 30px;
    margin-bottom: 38px;
    font-size: 18px;
    letter-spacing: 1.5px;
  }
  .field-label {
    width: 110px;
    flex: none;
  }
  .field-line {
    flex: 1;
    border-bottom: 1.5px solid var(--rule);
    height: 22px;
  }

  /* Contact block */
  .contact {
    position: absolute;
    left: 0;
    right: 0;
    top: 890px;
    text-align: center;
    font-size: 32px;
    letter-spacing: 3.5px;
    line-height: 1;
  }
  .contact p { margin: 0; }
  .phone { margin-bottom: 18px !important; }
  .address { line-height: 40px; }
  .website { margin-top: 8px !important; }
</style>
</head>
<body>
  <main class="card">
    <h1 class="brand">MotoSerenix</h1>
    <p class="specialty">Specializing in Asian, European and Domestic Auto Repair, Performance and Fabrication</p>

    <section class="appointment" aria-label="Appointment details">
      <h2 class="appointment-title">Your Appointment</h2>
      <div class="field"><span class="field-label">Date</span><span class="field-line"></span></div>
      <div class="field"><span class="field-label">Time</span><span class="field-line"></span></div>
      <div class="field"><span class="field-label">Advisor</span><span class="field-line"></span></div>
    </section>

    <section class="contact">
      <p class="phone">1-254-487-3106</p>
      <p class="address">4918 W. Birchwell Rd<br>Killeen, T.X. 76542</p>
      <p class="website">www.moto-serenix-example.com</p>
    </section>
  </main>
</body>
</html>
```